Lens Harbor Teutonia Website - Photography and Films

We are looking for a design that expresses the friendly, open nature of our company Lens Harbor Teutonia, yet at the same time is professional looking and functional.

Lens Harbor Teutonia is a B2B focused operation that hires out multi-lingual camera crews (and equipment) throughout Germany and Europe. We also produce tv features and coporate films. Our unique selling point is that we are native English speakers who can communicate with our international clients (usually British or American) and organise the logistics of shooting in foreign countries.

For content inspiration, see our current website: http://www.lensharborteutonia.com - however we want to move away from the very simple structure of this site and move towards a layout that displays and allows for frequently updated content (e.g. in the form of a blog).

Here is an example of the kind of clean look we like:
http://www.qrvpixelarchive.com/archive/main/reelsqrv.do#reel=48213760

Please keep within the following specifications:
- We wish to keep our logo (grey/white, font: Glypha) and our company colour red (#C40A0A) as they are.
- Maximum Width 960px, on a large browser-window the design should be centred
- Easily readable font sizes with good contrast
- Provide your design in PSD file format
- Our logo should be graphically displayed in the top left of the header.
- The design should allow space for a video.
- The page should have a clearly recognisable end in the form of a footer.

The following menu items need to be clearly arranged so the viewer is not overwhelmed or confused:
About
Services - Crews / Corporate Shoots / Webcasts / Production Arm / Legal Videography
Recent Productions
Blog
Testimonials
Get a Quote
Contact
Film Library
Showreel
Events
Film Location Guide - Frankfurt / Cologne / Zurich / Helsinki / Amsterdam / London / Paris / Rome / Brussels / Berlin / Munich
Updates

Reason: Hi - thanks very much for your interest in our design project.  We are extending this auction because we haven't had enough time to really focus on the desigs and provide immediate feedback to designers.  We will try to provide timely feedback and are giving you more time to make any adjustments to your designs etc.
Thanks!
Marla

Target Market(s)

Our target customers are males and females between 25 and 55 years (mostly British and American). More important than their demographic though, is their occupation - they are largely communication and design savvy individuals belonging to one of the following three categories: 1)Broadcasters (usually producers for example from the QRV or Horizon Vista TV seeking trustworthy, affordable crews for their foreign shoots).

2) Video Production Companies (seeking a trustworthy, affordable partner company to provide the crews for their own corporate clients).

3) Corporate Communications Specialists (seeking professional producers and crews to facilitate production of company videos or filming of events).

Industry/Entity Type

Camera

Requirements
Must have
• A fresh clean appearance with good use of white space.
Should not have
• Avoid dark heavy colours and designs.
• Avoid designs that would be impractical and could potentially take a long time to load.

```html
<!DOCTYPE html>
<html lang="en">
<head>
<meta charset="utf-8">
<title>Lens Harbor Teutonia</title>
<link rel="stylesheet" href="https://fonts.googleapis.com/css2?family=Roboto+Slab:wght@700;800&family=Arimo:wght@400;700&display=swap">
<style>
:root{
  --brand-red:#c40a0a;
  --brand-red-dark:#a30606;
  --accent-crimson:#c8102e;
  --ink:#1a1a1a;
  --text:#222;
  --grey-mid:#888;
  --grey-light:#e6e6e6;
  --panel:#ffffff;
  --page:#ffffff;
}
*{box-sizing:border-box;margin:0;padding:0}
html,body{width:1200px;height:821px;overflow:hidden;background:var(--page)}
body{font-family:"Arimo",Arial,sans-serif;color:var(--text)}
.stage{position:absolute;left:0;top:0;width:1147px;height:788px;transform:scale(1.0462,1.0419);transform-origin:0 0;
  background:linear-gradient(#d8d8d8 88px,#e9e9e9 140px,#f7f7f7 300px,#fff 420px)}
.abs{position:absolute}

/* header */
.site-header{left:0;top:0;width:1147px;height:88px;
  background:linear-gradient(100deg,#c40a0a 0%,#c40a0a 58%,#d61414 68%,#c70b0b 76%,#dc1a1a 86%,#c40a0a 100%);
  border-bottom:1px solid #8d0505}
.brand{left:83px;top:26px;font-family:"Roboto Slab",Georgia,serif;font-weight:800;font-size:38px;letter-spacing:-1.5px;color:#fff;line-height:1}
.top-nav{left:698px;top:45px;display:flex;height:43px;align-items:center;font-size:13px;color:#fff}
.top-nav a{color:#fff;text-decoration:none}
.top-nav .current{background:var(--brand-red-dark);height:43px;width:43px;display:flex;align-items:center;justify-content:center;margin-right:9px}
.top-nav .sep{margin:0 5px}

/* main nav */
.main-nav{left:83px;top:104px;font-size:15px;color:var(--ink);white-space:nowrap;display:flex}
.main-nav span{margin:0 7px}
.main-nav .active{background:#fff;color:var(--accent-crimson);padding:0 13px;margin:-3px 3px 0 -2px;height:27px;line-height:21px;border-radius:3px 3px 0 0;padding-top:3px}
.dropdown{left:130px;top:127px;width:167px;height:127px;background:rgba(255,255,255,.94);border-radius:0 3px 3px 3px;padding:8px 11px 0;font-size:14px;color:var(--ink)}
.dropdown li{list-style:none;height:23px;line-height:19px;border-bottom:1px solid #d8d8d8}
.dropdown li:last-child{border:0}

/* content panel */
.content-panel{left:81px;top:136px;width:998px;height:547px;background:var(--panel);border-radius:4px 4px 0 0;box-shadow:0 0 4px rgba(0,0,0,.15)}
.video-card{left:101px;top:157px;width:370px;height:502px;border:1px solid #cfcfcf;border-radius:4px;background:linear-gradient(#fff,#f4f4f4 60%,#fff);box-shadow:0 1px 3px rgba(0,0,0,.12)}
.video-frame{left:112px;top:167px;width:349px;height:243px;border-radius:4px;background:linear-gradient(160deg,#3c4a5c,#1c1f26 45%,#2c2622 80%,#4a3426)}
.controls{left:112px;top:416px;width:349px;height:44px}
.play{left:115px;top:418px}
.progress{left:157px;top:432px;width:140px;height:14px;border:1px solid #aaa;background:linear-gradient(#fff,#eee)}
.progress::before{content:"";position:absolute;left:0;top:0;width:4px;height:12px;background:#333}
.time{left:303px;top:433px;font-size:10px;color:#444}
.vol{left:362px;top:427px}
.card-divider{left:108px;top:470px;width:356px;height:2px;background:linear-gradient(90deg,transparent,#ddd,transparent)}
.audience-tabs{left:110px;top:485px;width:167px}
.audience-tabs li{list-style:none;height:50px;display:flex;align-items:center;gap:10px;padding-left:8px;background:#efefef;border-bottom:1px solid #fff;font-weight:700;font-size:14px;color:var(--accent-crimson);line-height:14px}
.audience-tabs li.on{background:#fff}
.audience-copy{left:277px;top:485px;width:190px;height:163px;background:#fff;padding:14px 14px 0;font-size:12px;line-height:14px}
.btn-small{display:inline-block;color:#fff;font-size:12px;padding:2px 8px;border-radius:2px}
.read-more{left:291px;top:614px;background:var(--accent-crimson)}

.intro-title{left:492px;top:153px;font-family:"Roboto Slab",Georgia,serif;font-weight:800;font-size:25px;line-height:26px;color:#000;letter-spacing:-.3px}
.intro-copy{left:495px;top:223px;width:595px;font-size:13px;line-height:16px;color:var(--text)}
.intro-copy p{margin-bottom:16px}
.quote-btn{left:494px;top:413px;width:111px;height:26px;border-radius:4px;background:linear-gradient(#e02222,#b30707);color:#fff;font-weight:700;font-size:14px;text-align:center;line-height:25px;box-shadow:0 2px 2px rgba(0,0,0,.25)}

.feed-head{height:34px;background:linear-gradient(90deg,#e7e7e7,#f4f4f4 70%,#fafafa);border-bottom:1px solid #aaa;font-weight:700;font-size:16px;color:#666;padding:7px 8px}
.feed-head::after{content:"";position:absolute;left:0;top:32px;width:137px;height:2px;background:#9a9a9a}
.blog{left:491px;top:463px;width:270px}
.news{left:782px;top:463px;width:270px}
.post{font-size:12px;line-height:14px;padding:11px 0 9px}
.post + .post{border-top:1px dotted #bbb}
.byline{color:var(--brand-red);font-weight:700}
.btn-grey{background:#8f8f8f}
.view-blog{left:492px;top:640px}
.view-all{left:782px;top:643px;width:72px;text-align:center}
.news-item{display:flex;gap:12px;margin-top:11px;font-size:12px;line-height:14px}
.thumb{width:66px;height:58px;flex:none;border:4px solid #eee;box-shadow:0 0 2px rgba(0,0,0,.2);background:linear-gradient(150deg,#8b8f93,#3b3d40 60%,#6a5a4e)}
.news-item h3{font-size:12px;color:var(--accent-crimson);margin:3px 0 1px}

/* footer */
.site-footer{left:81px;top:683px;width:998px;height:82px;background:linear-gradient(#e2e2e2,#f2f2f2 40%,#fafafa);border-top:1px solid #bcbcbc;box-shadow:0 2px 4px rgba(0,0,0,.1)}
.footer-brand{left:101px;top:694px;font-family:"Roboto Slab",Georgia,serif;font-weight:800;font-size:19px;color:#9a9a9a}
.footer-info{left:101px;top:722px;font-size:12px;line-height:14px;color:#222}
.footer-info u{text-decoration:none;border-bottom:1px solid #444}
.social{top:697px;width:30px;height:30px;border-radius:3px}
.social.one{left:995px;background:linear-gradient(#bfe7f7,#6cc3e8)}
.social.two{left:1034px;background:linear-gradient(#5b78b4,#35508f)}
</style>
</head>
<body>
<div class="stage">
  <header class="site-header abs"></header>
  <div class="brand abs">lensharborteutonia</div>
  <nav class="top-nav abs">
    <a class="current">home</a><a>showreel</a><span class="sep">|</span><a>production arm</a><span class="sep">|</span><a>legal videography</a><span class="sep">|</span><a>contact</a>
  </nav>

  <nav class="main-nav abs">
    <span style="margin-left:0">About</span><span class="active">Services</span><span style="margin-left:0">Recent Productions</span>|<span>Blog</span>|<span>Testimonials</span>|<span>Get a Quote</span>|<span>Contact</span>|<span>Film Library</span>|<span>Showreel</span>|<span>Events</span>|<span>Film Location Guide</span>
  </nav>

  <main class="content-panel abs"></main>

  <section class="video-card abs"></section>
  <div class="video-frame abs" role="img" aria-label="Video still: a crew filming on a conference stage set"></div>
  <svg class="play abs" width="40" height="40" viewBox="0 0 40 40"><defs><linearGradient id="g" x1="0" y1="0" x2="0" y2="1"><stop offset="0" stop-color="#fff"/><stop offset="1" stop-color="#ccc"/></linearGradient></defs><circle cx="20" cy="20" r="19" fill="url(#g)" stroke="#aaa"/><path d="M15 11 L29 20 L15 29 Z" fill="#333"/></svg>
  <div class="progress abs"></div>
  <div class="time abs">0:00 / 0:00</div>
  <svg class="vol abs" width="98" height="22" viewBox="0 0 98 22"><circle cx="10" cy="11" r="9" fill="#ddd" stroke="#aaa"/><rect x="6" y="10" width="8" height="2" fill="#333"/><g fill="#bbb"><rect x="28" y="8" width="4" height="7"/><rect x="35" y="7" width="4" height="9"/><rect x="42" y="6" width="4" height="11"/><rect x="49" y="5" width="4" height="13"/><rect x="56" y="4" width="4" height="15"/><rect x="63" y="3" width="4" height="17"/></g><circle cx="87" cy="11" r="9" fill="#ddd" stroke="#aaa"/><rect x="83" y="10" width="8" height="2" fill="#333"/><rect x="86" y="7" width="2" height="8" fill="#333"/></svg>
  <div class="card-divider abs"></div>

  <ul class="audience-tabs abs">
    <li class="on"><svg width="26" height="26" viewBox="0 0 26 26"><ellipse cx="13" cy="14" rx="11" ry="8" fill="#c6c6c6" transform="rotate(-35 13 14)"/><line x1="13" y1="14" x2="22" y2="4" stroke="#c6c6c6" stroke-width="2"/></svg>Video<br>broadcasters</li>
    <li><svg width="26" height="26" viewBox="0 0 26 26"><circle cx="13" cy="13" r="11" fill="#c6c6c6"/><g fill="#fff"><circle cx="13" cy="7" r="2.5"/><circle cx="13" cy="19" r="2.5"/><circle cx="7" cy="13" r="2.5"/><circle cx="19" cy="13" r="2.5"/></g></svg>video production<br>companies</li>
    <li><svg width="26" height="26" viewBox="0 0 26 26"><g fill="#c6c6c6"><circle cx="9" cy="7" r="4"/><path d="M2 20c0-5 3-8 7-8s7 3 7 8z"/><circle cx="18" cy="11" r="3.5"/><path d="M12 24c0-4 3-7 6-7s6 3 6 7z"/></g></svg>communications<br>specialists</li>
  </ul>
  <div class="audience-copy abs">Lorem ipsum dolor sit amet, consectetur adipiscing elit. Quisque eu bibendum mi. Donec sem elit, posuere quis egestas ut, fermentum ac metus. Cum sociis natoque. Aliquam erat volutpat.</div>
  <a class="btn-small read-more abs">read more</a>

  <h1 class="intro-title abs">english speaking camera crews<br>throughout germany and europe</h1>
  <div class="intro-copy abs">
    <p>We set up Lens Harbor Teutonia to meet the demands of a growing number of TV-producers whose working language is English. This is our Passion! Why else would we keep doing it for over 30 years!</p>
    <p>As a producer, you’re bound to have great ideas…but how do you make them a reality in a coun-<br>try where you can’t speak the language? Partner with us!</p>
    <p>We are native English speakers so nothing gets lost in translation. We’ll catch hold of your vision, and with local know-how, we’ll make it happen.</p>
    <p>No job is too big, too small, too hard, too far away, or too urgent. Try us!</p>
  </div>
  <a class="quote-btn abs">get a quote</a>

  <section class="blog abs">
    <h2 class="feed-head" style="position:relative">from the blog</h2>
    <div class="post">Lorem ipsum dolor sit amet, consectetur adipisc-ing elit. Nulla feugiat fringilla bibendum. Curabitur facilisis ligula at elit malesuada fringilla.<br><span class="byline">Posted by Dana @ October 18th, 2010</span></div>
    <div class="post">Curabitur facilisis ligula at elit malesuada fringilla. Aliquam erat volutpat. Aliquam erat volutpat Nulla feugiat fringilla bibendum.<br><span class="byline">Posted by Dana @ October 15th, 2010</span></div>
  </section>
  <a class="btn-small btn-grey view-blog abs">view blog</a>

  <section class="news abs">
    <h2 class="feed-head" style="position:relative">news &amp; events</h2>
    <div class="news-item" style="margin-top:11px"><div class="thumb" role="img" aria-label="Photo of a crew operating a camera"></div><div><h3>Lorem ipsum dolor sit amet</h3>consectetur adipiscing elit. Nulla feugiat fringilla bibendum.</div></div>
    <div class="news-item"><div class="thumb" role="img" aria-label="Photo of a camera operator on location"></div><div><h3>Consectetur adipiscing elit</h3>Nulla feugiat fringilla bibendum. Fusce non urna sed ligula .</div></div>
  </section>
  <a class="btn-small btn-grey view-all abs">view all</a>

  <footer class="site-footer abs"></footer>
  <div class="footer-brand abs">© lens harbor teutonia</div>
  <div class="footer-info abs">c/o Brightmoor Films • Kastanienweg 18 • 60311 Frankfurt/Main • Germany • info@lens-harbor-teutonia.com<br>Tel.: +49-69-555010 • Toll free from the USA 1-800-555-0142 &nbsp;| &nbsp;<u>Disclaimer</u></div>
  <a class="social one abs" aria-label="Social link"></a>
  <a class="social two abs" aria-label="Social link"></a>

  <ul class="dropdown abs">
    <li>Crews</li><li>Corporate Shoots</li><li>Webcasts</li><li>Production Arm</li><li>Legal Videography</li>
  </ul>
</div>
</body>
</html>
```